Mobile Oil Change company needs a flyer to promote new business

We need a flyer to 1) print & handout and 2) email out to potential customers. We are a mobile oil change company that comes to our customer locations to perform the work instead of customers going to traditional oil change companies. We have a 21 point inspection with our oil change. (21 point inspection details will not be on the flyer). Would like to keep the flyer simple but creative. I'm attaching 1) the write-up we created, 2) our logo (logo color is dark teal on white but other combinations are included if you wanted to propose a different color combination), and 3) additional services we offer. Logo font is Alegreya Sans.
Would like the additional services listed with icons and brief descriptions (similar to attachment) without pricing. Company website for reference is www.brindlefleetcare.com.

Target Market(s)

Companies with many service vehicles such as Oil & Gas service companies, heating and air conditioning companies, utility companies, police departments, etc. Companies that prioritize convenience and maintenance first.

Font styles to use
Sans Serif

Colors
00a990

Requirements
Must have
• Simple but creative design with our logo at top of the flyer. Additional Services (details in document supplied) can be smaller and less prominent than other "main" content listed in the CONTENT document supplied.
Should not have
• Do not use animated character graphics in the flyer and limit (1) stock photos to A small area in the flyer.

```html
<!DOCTYPE html>
<html lang="en">
<head>
<meta charset="utf-8">
<title>Brindle Fleet Care – Mobile Oil Change Flyer</title>
<link rel="stylesheet" href="https://fonts.googleapis.com/css2?family=Signika:wght@300;400;600&display=swap">
<style>
  :root {
    --teal: #2f8d7d;
    --teal-light: #3c9c8b;
    --mint: #c5e2da;
    --ink: #1c2626;
    --red: #d9262c;
    --white: #ffffff;
    --black: #0c0c0c;
  }
  * { margin: 0; padding: 0; box-sizing: border-box; }
  html, body { width: 849px; height: 1200px; overflow: hidden; background: var(--white); }
  body { font-family: "Signika", sans-serif; color: var(--ink); }
  .flyer { position: relative; width: 849px; height: 1200px; overflow: hidden; }
  .backdrop { position: absolute; inset: 0; }

  .brand {
    position: absolute; left: 38px; top: 34px;
    display: flex; align-items: center; gap: 10px;
    color: var(--white); font-weight: 600; font-size: 26px; line-height: 1.05;
  }
  .brand-square { width: 14px; height: 14px; background: var(--white); flex: none; }
  .headline {
    position: absolute; left: 269px; top: 36px; width: 552px;
    color: var(--white); font-weight: 600; font-size: 32.5px; line-height: 40px; white-space: nowrap;
  }

  .process-title {
    position: absolute; left: 0; top: 564px; width: 849px;
    text-align: center; font-weight: 600; font-size: 23.5px; line-height: 27px;
  }

  .steps { position: absolute; left: 38px; top: 645px; list-style: none; }
  .step { display: flex; align-items: center; gap: 6px; font-weight: 300; font-size: 14.6px; line-height: 17px; height: 39px; white-space: nowrap; }
  .step-icon { width: 32px; height: 32px; flex: none; }

  .features { position: absolute; top: 0; left: 0; list-style: none; }
  .feature { position: absolute; display: flex; gap: 9px; font-weight: 300; font-size: 14px; line-height: 16.5px; white-space: nowrap; }
  .feature svg { width: 11px; height: 11px; margin-top: 3px; flex: none; }

  .call-box {
    position: absolute; left: 74px; top: 1118px; height: 44px;
    display: flex; border: 1.5px solid var(--black);
  }
  .call-label { background: var(--black); color: var(--white); font-weight: 600; font-size: 24px; width: 164px; display: flex; align-items: center; justify-content: center; }
  .call-number { background: var(--white); font-weight: 600; font-size: 20px; width: 167px; display: flex; align-items: center; justify-content: center; }

  .contacts { position: absolute; right: 12px; top: 1117px; text-align: right; font-size: 14.5px; line-height: 24px; white-space: nowrap; }
  .contact-label { font-weight: 600; text-decoration: underline; color: var(--ink); }
  .contact-value { color: var(--red); }
</style>
</head>
<body>
<div class="flyer">
  <svg class="backdrop" width="849" height="1200" viewBox="0 0 849 1200">
    <defs>
      <linearGradient id="header-band" x1="0" y1="0" x2="1" y2="0">
        <stop offset="0" stop-color="#2e8a7a"/>
        <stop offset="1" stop-color="#3a9a89"/>
      </linearGradient>
      <linearGradient id="engine-tone" x1="0" y1="0" x2="1" y2="1">
        <stop offset="0" stop-color="#3a3d42"/>
        <stop offset="0.6" stop-color="#2c3036"/>
        <stop offset="1" stop-color="#454a52"/>
      </linearGradient>
      <linearGradient id="pour-tone" x1="0" y1="0" x2="1" y2="1">
        <stop offset="0" stop-color="#3f7fa8"/>
        <stop offset="0.5" stop-color="#9c7a3c"/>
        <stop offset="1" stop-color="#34373c"/>
      </linearGradient>
      <linearGradient id="tech-tone" x1="0" y1="0" x2="1" y2="0">
        <stop offset="0" stop-color="#eeebe6"/>
        <stop offset="0.5" stop-color="#ead98a"/>
        <stop offset="1" stop-color="#ecd45a"/>
      </linearGradient>
      <linearGradient id="bottle-tone" x1="0" y1="0" x2="1" y2="0">
        <stop offset="0" stop-color="#77797b"/>
        <stop offset="0.45" stop-color="#cdbb84"/>
        <stop offset="1" stop-color="#eeebe6"/>
      </linearGradient>
    </defs>

    <rect x="0" y="0" width="849" height="113" fill="url(#header-band)"/>

    <g role="img" aria-label="Photo: oil being poured through a red funnel into a car engine">
      <rect x="0" y="113" width="849" height="429" fill="url(#engine-tone)"/>
    </g>
    <polygon points="0,216 448,542 416,542 0,240" fill="var(--mint)"/>
    <g role="img" aria-label="Photo: golden motor oil pouring from a blue bottle">
      <polygon points="0,240 416,542 0,542" fill="url(#pour-tone)"/>
    </g>

    <rect x="0" y="542" width="849" height="87" fill="var(--mint)"/>
    <polygon points="155,629 175,629 165,641" fill="var(--mint)"/>

    <g role="img" aria-label="Photo: technician in a yellow shirt holding a wrench">
      <polygon points="544,629 849,629 849,856 400,856" fill="url(#tech-tone)"/>
    </g>

    <g role="img" aria-label="Photo: motor oil pouring from a grey bottle">
      <polygon points="0,856 400,856 532,1079 0,1079" fill="url(#bottle-tone)"/>
    </g>

    <rect x="0" y="1079" width="849" height="121" fill="var(--mint)"/>
    <polygon points="532,1079 546,1079 628,1200 614,1200" fill="var(--white)"/>
    <rect x="0" y="1078" width="532" height="2" fill="var(--black)"/>
  </svg>

  <div class="brand"><span class="brand-square"></span><span>Brindle<br>Fleet Care</span></div>
  <h1 class="headline">Hassle free oil changes on your terms</h1>

  <h2 class="process-title">Our simple 5-step process lets you schedule an appointment and get<br>service to save time and money</h2>

  <ol class="steps">
    <li class="step">
      <svg class="step-icon" viewBox="0 0 32 32"><rect x="6" y="6" width="20" height="20" transform="rotate(45 16 16)" fill="none" stroke="var(--red)" stroke-width="1.4"/><rect x="11" y="12" width="10" height="8" fill="none" stroke="var(--red)" stroke-width="1.2"/><path d="M11 12l5 4 5-4" fill="none" stroke="var(--red)" stroke-width="1.2"/></svg>
      Call or email us to schedule service
    </li>
    <li class="step">
      <svg class="step-icon" viewBox="0 0 32 32"><rect x="6" y="6" width="20" height="20" transform="rotate(45 16 16)" fill="none" stroke="var(--red)" stroke-width="1.4"/><path d="M11 11l10 10M21 11l-10 10" stroke="var(--red)" stroke-width="1.4"/></svg>
      Our highly trained technicians come to you for service
    </li>
    <li class="step">
      <svg class="step-icon" viewBox="0 0 32 32"><rect x="6" y="6" width="20" height="20" transform="rotate(45 16 16)" fill="none" stroke="var(--red)" stroke-width="1.4"/><rect x="10" y="14" width="12" height="5" rx="1" fill="none" stroke="var(--red)" stroke-width="1.2"/><circle cx="13" cy="20" r="1.3" fill="var(--red)"/><circle cx="19" cy="20" r="1.3" fill="var(--red)"/></svg>
      Service is performed quickly on your vehicle
    </li>
    <li class="step">
      <svg class="step-icon" viewBox="0 0 32 32"><rect x="6" y="6" width="20" height="20" transform="rotate(45 16 16)" fill="none" stroke="var(--red)" stroke-width="1.4"/><circle cx="16" cy="13" r="3" fill="none" stroke="var(--red)" stroke-width="1.2"/><path d="M10 20h9l3-2" fill="none" stroke="var(--red)" stroke-width="1.2"/></svg>
      Pay agreed-upon pricing and receipt is emailed to you
    </li>
    <li class="step">
      <svg class="step-icon" viewBox="0 0 32 32"><rect x="6" y="6" width="20" height="20" transform="rotate(45 16 16)" fill="none" stroke="var(--red)" stroke-width="1.4"/><path d="M16 22s-4-4-4-7a4 4 0 018 0c0 3-4 7-4 7z" fill="none" stroke="var(--red)" stroke-width="1.2"/><circle cx="16" cy="15" r="1.3" fill="var(--red)"/></svg>
      <span>Services performed are tracked electronically and<br>reminders created</span>
    </li>
  </ol>

  <ul class="features">
    <li class="feature" style="left:469px; top:898px;">
      <svg viewBox="0 0 12 12"><rect x="0.6" y="0.6" width="10.8" height="10.8" fill="none" stroke="var(--red)" stroke-width="1"/><path d="M2.5 6l2.5 2.5L10 2" fill="none" stroke="var(--red)" stroke-width="1.3"/></svg>
      <span>High quality synthetic oil used is best suited<br>for commercial vehicles</span>
    </li>
    <li class="feature" style="left:502px; top:958px;">
      <svg viewBox="0 0 12 12"><rect x="0.6" y="0.6" width="10.8" height="10.8" fill="none" stroke="var(--red)" stroke-width="1"/><path d="M2.5 6l2.5 2.5L10 2" fill="none" stroke="var(--red)" stroke-width="1.3"/></svg>
      <span>Service includes a 21-point inspection</span>
    </li>
    <li class="feature" style="left:534px; top:1008px;">
      <svg viewBox="0 0 12 12"><rect x="0.6" y="0.6" width="10.8" height="10.8" fill="none" stroke="var(--red)" stroke-width="1"/><path d="M2.5 6l2.5 2.5L10 2" fill="none" stroke="var(--red)" stroke-width="1.3"/></svg>
      <span>Additional services are available</span>
    </li>
  </ul>

  <div class="call-box">
    <div class="call-label">Call now at</div>
    <div class="call-number">(833) 555-0142</div>
  </div>

  <div class="contacts">
    <div><span class="contact-label">Email</span> : <span class="contact-value">Sales@BrindleFleetCare.com</span></div>
    <div><span class="contact-label">Website</span> : <span class="contact-value">www.BrindleFleetCare.com</span></div>
  </div>
</div>
</body>
</html>
```